French Tech Blog : Wordpress theme

I need a wordpress theme made, for a french tech blog like gizmoharbor.com or plankdollar.com .. (the structure)

I will of course also need a logo that hold the identity of the website !

The blog's name is GalletMirage.com

The tone should be in the dark blue..

Target Market(s)

affiliate marketers, web entrepreneurs, 70% male between 20 and 35

Industry/Entity Type

Tech

```html
<!DOCTYPE html>
<html lang="en">
<head>
<meta charset="utf-8">
<title>Gallet Mirage — Tech Blog</title>
<link href="https://fonts.googleapis.com/css2?family=Ubuntu:wght@400;500;700&display=swap" rel="stylesheet">
<style>
:root{
  --navy:#0d1f3f;
  --blue:#0f5aa0;
  --blue-light:#1a78c8;
  --ink:#1c2333;
  --muted:#6b7380;
  --rule:#e3e6ea;
  --red:#d4203f;
  --red-deep:#e0001b;
  --bg:#0d4677;
}
*{box-sizing:border-box;margin:0;padding:0}
html,body{width:880px;height:1200px;overflow:hidden}
body{position:relative;font-family:"Ubuntu",sans-serif;color:var(--ink);
  background:radial-gradient(ellipse at 50% 40%,#1767a8 0%,var(--bg) 55%,#06274a 100%)}
.abs{position:absolute}
.header{left:56px;top:0;width:768px;height:124px;background:#fff}
.brand{left:82px;top:38px;display:flex;align-items:center;gap:10px}
.brand-dot{width:34px;height:34px;border-radius:50%;background:var(--red)}
.brand-name{font-size:28px;font-weight:500;color:var(--navy);line-height:1}
.network{left:378px;top:20px;width:432px;height:48px;background:#151515;color:#fff;padding:4px 8px;font-size:6.4px;line-height:8px}
.network h2{font-size:10.4px;color:#3aa6e8;font-weight:700;margin-bottom:2px}
.network .cols{display:flex;gap:22px}
.network .bars{position:absolute;right:6px;bottom:4px}
.nav{left:56px;top:124px;width:768px;height:35px;background:var(--navy)}
.nav .home{left:0;top:0;width:118px;height:35px;background:linear-gradient(#1b6fb8,#1160a8)}
.nav a{position:absolute;top:11px;color:#fff;font-size:11px;text-decoration:none;letter-spacing:.3px}
.search{left:646px;top:133px;width:161px;height:19px;background:#fff}
.main{left:56px;top:159px;width:768px;height:875px;background:#fff}
.vrule{left:564px;top:165px;width:1px;height:862px;background:var(--rule)}
.hero{left:67px;top:171px;width:488px;height:232px;background:radial-gradient(circle at 55% 45%,#8cc6e4 0%,#2b7fae 35%,#0c3a5c 100%)}
.post{left:67px;width:488px;height:140px}
.post h3{position:absolute;left:1px;top:0;font-size:14.5px;font-weight:400;letter-spacing:.3px}
.post .thumb{position:absolute;left:0;top:28px;width:93px;height:65px;background:linear-gradient(135deg,#a7b8bf,#2f7d87 55%,#1b4f5a)}
.post p{position:absolute;left:99px;width:389px;font-size:9.3px;line-height:13px;color:var(--muted);letter-spacing:.15px}
.post .p1{top:29px}.post .p2{top:62px}
.btn-more{position:absolute;left:99px;top:96px;width:55px;height:17px;border-radius:3px;background:var(--blue);color:#fff;font-size:7.5px;font-weight:700;text-align:center;line-height:17px}
.share{position:absolute;left:380px;top:101px;width:100px;height:10px;border:1px solid #c9cdd2;border-radius:2px;font-size:6.4px;line-height:8px;padding-left:18px;letter-spacing:.6px}
.share i{position:absolute;left:3px;top:1px;width:7px;height:6px;background:var(--red)}
.share b{position:absolute;top:1px;width:7px;height:6px;border-radius:1px}
.post hr{position:absolute;left:0;top:128px;width:486px;border:0;border-top:1px solid var(--rule)}
.social{left:584px;top:172px;display:flex;gap:7.5px}
.social span{width:25px;height:24px;border-radius:4px}
.cta{left:582px;width:216px;height:39px;border:1px solid #dde0e4;font-size:8.8px;font-weight:700;padding-left:37px;line-height:38px;color:#111}
.cta i{position:absolute;left:10px;top:10px;width:19px;height:19px;border-radius:50%}
.tabs{left:570px;top:315px;width:245px;height:168px;background:var(--blue)}
.tab{position:absolute;top:7px;font-size:11px;color:#fff}
.tab.active{left:8px;top:4px;width:67px;height:17px;background:#fff;color:var(--ink);padding:2px 0 0 6px}
.tab-panel{left:9px;top:21px;width:230px;height:140px;background:#fff;padding:12px 0 0 8px}
.arrow-list{list-style:none}
.arrow-list li{position:relative;padding-left:14px;font-size:9.3px;color:var(--muted);letter-spacing:.3px}
.arrow-list li::before{content:"";position:absolute;left:0;top:4px;border-left:5px solid #111;border-top:3px solid transparent;border-bottom:3px solid transparent}
.arrow-list li::after{content:"";position:absolute;left:-3px;top:5.5px;width:4px;height:3px;background:#111}
.tab-panel li{height:13px}
.side-head{left:571px;width:245px;height:26px;background:var(--blue);color:#fff;font-size:11px;padding:7px 0 0 9px;letter-spacing:.3px}
.featured{left:581px;top:543px;width:235px}
.featured li{line-height:13px;margin-bottom:6px}
.fans{left:601px;top:708px;width:185px;height:225px;border:1px solid #ccc;background:linear-gradient(#b9c9d6 0%,#a99a82 45%,#4d4f55 100%)}
.badge{top:952px;width:80px;height:74px}
.footer{left:56px;top:1034px;width:768px;height:132px;background:var(--red)}
.fcol{top:1046px;color:#fff}
.fcol h4{font-size:13.5px;font-weight:400;margin-bottom:5px}
.fcol li{list-style:none;font-size:9.8px;line-height:14.4px;letter-spacing:.3px}
.fsep{top:1048px;width:1px;height:102px;background:rgba(255,255,255,.18)}
.newsletter{left:596px;top:1041px;width:219px;height:120px;background:var(--red-deep);color:#fff;padding:6px 0 0 9px}
.newsletter h4{font-size:13.5px;font-weight:400}
.field{left:70px;width:144px;height:20px;background:#fff}
.flabel{left:10px;font-size:10.5px}
.signup{left:149px;top:81px;width:63px;height:24px;border-radius:4px;background:linear-gradient(#2d8ce0,#0c55a7);color:#fff;font-size:11px;font-weight:700;text-align:center;line-height:24px}
.copy{left:57px;top:1176px;font-size:9.6px;color:#9fb3c8;letter-spacing:.3px}
.copy b{color:#fff;font-weight:400}
</style>
</head>
<body>
<div class="abs header"></div>
<div class="abs brand"><span class="brand-dot"></span><span class="brand-name">Gallet Mirage</span></div>
<div class="abs network">
  <h2>The Corvane News Network</h2>
  <div class="cols">
    <div>• 750,000 visitors access network content per month<br>• 89,660 subscribers receive email updates<br>• 10,000+ domains access network content</div>
    <div>• Advertising Opportunities<br>• Content Management &amp; Delivery<br>• Press Release Distribution</div>
  </div>
  <svg class="bars" width="70" height="38" viewBox="0 0 70 38"><rect x="6" y="26" width="10" height="12" fill="#1c7cc8"/><rect x="20" y="18" width="10" height="20" fill="#2590de"/><rect x="34" y="10" width="10" height="28" fill="#2e9ee9"/><rect x="48" y="2" width="10" height="36" fill="#3ab0f5"/></svg>
</div>

<nav class="abs nav">
  <div class="abs home"></div>
  <a style="left:43px">HOME</a>
  <a style="left:154px">ABOUT US</a>
  <a style="left:255px">TECH RESOURCES</a>
  <a style="left:410px">CONTACT US</a>
</nav>
<div class="abs search">
  <svg class="abs" style="left:143px;top:3px" width="13" height="13" viewBox="0 0 13 13"><circle cx="5.5" cy="5.5" r="4" fill="none" stroke="#1a78c8" stroke-width="2"/><line x1="8.5" y1="8.5" x2="12" y2="12" stroke="#1a78c8" stroke-width="2.4"/></svg>
</div>

<div class="abs main"></div>
<div class="abs vrule"></div>
<div class="abs hero" role="img" aria-label="Hand touching a glowing blue interface of floating squares"></div>

<article class="abs post" style="top:414px">
  <h3>The world of opportunities</h3>
  <div class="thumb" role="img" aria-label="Teal field of floating binary digits"></div>
  <p class="p1">Lorem ipsum dolor sit amet conse ctetuer adipiscing elit. Praeslum molestie lacu-sean nonummyendrerit mausellus porta. Fusce suscipit varius mium sociis natus.</p>
  <p class="p2">Fuscefeu giat malesuada odiorbi nunc odio gravitcursus necuctus a loremecenas tristique orci ac sem. Duis ultricies pharetra magn accumsan malesuada orci.</p>
  <div class="btn-more">Read More</div>
  <div class="share"><i></i>SHARE<b style="left:62px;background:#3aa6e8"></b><b style="left:71px;background:#2f5fa8"></b><b style="left:80px;background:#b0306a"></b></div>
  <hr>
</article>
<article class="abs post" style="top:556px">
  <h3>The world of opportunities</h3>
  <div class="thumb" role="img" aria-label="Teal field of floating binary digits"></div>
  <p class="p1">Lorem ipsum dolor sit amet conse ctetuer adipiscing elit. Praeslum molestie lacu-sean nonummyendrerit mausellus porta. Fusce suscipit varius mium sociis natus.</p>
  <p class="p2">Fuscefeu giat malesuada odiorbi nunc odio gravitcursus necuctus a loremecenas tristique orci ac sem. Duis ultricies pharetra magn accumsan malesuada orci.</p>
  <div class="btn-more">Read More</div>
  <div class="share"><i></i>SHARE<b style="left:62px;background:#3aa6e8"></b><b style="left:71px;background:#2f5fa8"></b><b style="left:80px;background:#b0306a"></b></div>
  <hr>
</article>
<article class="abs post" style="top:703px">
  <h3>The world of opportunities</h3>
  <div class="thumb" role="img" aria-label="Teal field of floating binary digits"></div>
  <p class="p1">Lorem ipsum dolor sit amet conse ctetuer adipiscing elit. Praeslum molestie lacu-sean nonummyendrerit mausellus porta. Fusce suscipit varius mium sociis natus.</p>
  <p class="p2">Fuscefeu giat malesuada odiorbi nunc odio gravitcursus necuctus a loremecenas tristique orci ac sem. Duis ultricies pharetra magn accumsan malesuada orci.</p>
  <div class="btn-more">Read More</div>
  <div class="share"><i></i>SHARE<b style="left:62px;background:#3aa6e8"></b><b style="left:71px;background:#2f5fa8"></b><b style="left:80px;background:#b0306a"></b></div>
  <hr>
</article>
<article class="abs post" style="top:848px">
  <h3>The world of opportunities</h3>
  <div class="thumb" role="img" aria-label="Teal field of floating binary digits"></div>
  <p class="p1">Lorem ipsum dolor sit amet conse ctetuer adipiscing elit. Praeslum molestie lacu-sean nonummyendrerit mausellus porta. Fusce suscipit varius mium sociis natus.</p>
  <p class="p2">Fuscefeu giat malesuada odiorbi nunc odio gravitcursus necuctus a loremecenas tristique orci ac sem. Duis ultricies pharetra magn accumsan malesuada orci.</p>
  <div class="btn-more">Read More</div>
  <div class="share"><i></i>SHARE<b style="left:62px;background:#3aa6e8"></b><b style="left:71px;background:#2f5fa8"></b><b style="left:80px;background:#b0306a"></b></div>
  <hr>
</article>

<div class="abs social">
  <span style="background:#5fb6e0"></span><span style="background:#555"></span><span style="background:#3b63a8"></span><span style="background:#2f6eb0"></span><span style="background:#3e9a3a"></span>
  <svg width="25" height="24" viewBox="0 0 24 24"><polygon points="12,1 15,9 23,9 16.5,14 19,22 12,17 5,22 7.5,14 1,9 9,9" fill="#f4b922"/></svg>
  <svg width="25" height="24" viewBox="0 0 24 24"><rect width="24" height="24" rx="4" fill="#3ea83a"/><rect x="10" y="4" width="4" height="16" fill="#fff"/><rect x="4" y="10" width="16" height="4" fill="#fff"/></svg>
</div>
<div class="abs cta" style="top:207px"><i style="background:#f08a1c"></i>SUBSCRIBE TO OUR RSS FEED!</div>
<div class="abs cta" style="top:254px"><i style="background:#4aaee6"></i>FOLLOW US ON CHIRPER!</div>

<div class="abs tabs">
  <div class="tab active">Category</div>
  <div class="tab" style="left:91px">Archives</div>
  <div class="tab" style="left:162px">Comments</div>
  <div class="abs tab-panel">
    <ul class="arrow-list">
      <li>Browsers</li><li>Computers</li><li>Featured</li><li>General</li><li>News</li><li>Parent Categor</li><li>Child Category</li><li>Tech</li><li>Lorem Ipsum is simply</li>
    </ul>
  </div>
</div>

<div class="abs side-head" style="top:504px">Featured Posts</div>
<ul class="abs arrow-list featured">
  <li>Sample post with, links, paragraphs and com-ments..</li>
  <li>This is Just Going To Be Another Test Post..</li>
  <li>Keeping The Title Length Equal For Home..</li>
  <li>Another One to Fill Space..</li>
  <li>This Is Going To Be A Decent Length Title With Little Text..</li>
</ul>

<div class="abs side-head" style="top:676px">Gallet Mirage Friends &amp; Fans</div>
<div class="abs fans" role="img" aria-label="Group of friends posing in front of a clock tower"></div>
<div class="abs badge" style="left:602px;background:linear-gradient(#e9f0e4,#3b86c9)" role="img" aria-label="Partner badge"></div>
<div class="abs badge" style="left:703px;background:#2a2a2a" role="img" aria-label="Partner badge"></div>

<footer class="abs footer"></footer>
<div class="abs fcol" style="left:68px"><h4>Reviews</h4><ul style="padding-left:2px"><li>Tech</li><li>online marketing</li><li>Afiliation</li><li>Making Money</li></ul></div>
<div class="abs fsep" style="left:176px"></div>
<div class="abs fcol" style="left:198px"><h4>News</h4><ul><li>Business Tech</li><li>Corrections</li><li>Crave</li><li>Green Tech</li><li>Wireless</li></ul></div>
<div class="abs fsep" style="left:293px"></div>
<div class="abs fcol" style="left:317px"><h4>Downloads</h4><ul><li>Windows</li><li>Mac</li><li>Webware</li><li>All Downloads</li><li>Add your software</li></ul></div>
<div class="abs fsep" style="left:429px"></div>
<div class="abs fcol" style="left:454px"><h4>More</h4><ul><li>About Netwave</li><li>Netwave Forums</li><li>About Halden Interactive</li><li>Center</li><li>Customer Help</li></ul></div>
<div class="abs newsletter">
  <h4>Newsletter</h4>
  <span class="abs flabel" style="top:36px">Emial id</span>
  <div class="abs field" style="top:25px"></div>
  <span class="abs flabel" style="top:61px">Password</span>
  <div class="abs field" style="top:50px"></div>
  <div class="abs signup">Sign Up ▸</div>
</div>
<div class="abs copy">Copyright © <b>Gallet Mirage</b></div>
</body>
</html>
```